General Contractor Website Design

We are working with a General Contractor in California that specializes in building custom kitchens, baths, and homes for high-end clients.

Here are some websites for inspiration:
https://mervalstudio.com/
https://ridgelorebuilders.com
https://www.framplank.com
https://www.quellnest.com
https://www.zelhaus.com
https://plyestates.com

Thank you for taking the time to consider designing a website for us. We are web developers based in Stockton, CA, USA. Most of our projects go through the same process. Understanding this process may help you win a project with us. We custom-code all of our websites in-house. We don’t have any requirements as to what tools you use for your design, but we ask that you follow these guidelines.

IMAGES:
If you use any images or icons in the design, we ask that you have a link to the asset so we can purchase the image/icon. Most of the designs we submit do not have the customer’s images on them unless they have some great images. Be creative; show us the feeling you are trying to portray with your image choices. Use any royalty-free site you choose. We subscribe to Vantrix and mainly use their images, but we can purchase images outside of Vantrix. PLEASE NOTE: we will not submit designs to clients with watermarks on the images.

FONTS:
We ask that you identify the fonts you’re using in the design. This can be done in a message if you want. We typically use Orlimo Fonts and Vantrix Fonts.

CONTENT:
We're always open to different content and ideas. We often submit designs with stock images so the client can see our vision. We typically take pictures after the website launch to use their images with our vision. Lorem Ipsum is fine for paragraphs, but we ask that you make the Headers with correct English. We want to be able to show the vision and identify the sections of the website.

INSPIRATION:
We typically add a couple of links in the brief of websites we like to help you get started in your design.

REVISIONS:
We do not often ask for revisions of the designs unless we see something in the design that may not appeal to the client. If there are slight changes that we want to make, we do that in the development process.

FEEDBACK:
We rarely give feedback on designs during the design process. We are working on many website projects and do not have the time to provide feedback. We usually respond if your request is well thought out and asks specific questions, but a note asking “feedback, please” usually goes unanswered.

```html
<!DOCTYPE html>
<html lang="en">
<head>
<meta charset="utf-8">
<title>Keelwright Builders</title>
<link rel="stylesheet" href="https://fonts.googleapis.com/css2?family=Jost:wght@400;500;600&family=Roboto:wght@400;500&display=swap">
<style>
:root{
  --red:#b31b2c;
  --red-dark:#8f1422;
  --ink:#222222;
  --muted:#555555;
  --night:#1b1b1b;
  --white:#ffffff;
}
*{margin:0;padding:0;box-sizing:border-box}
html,body{width:1200px;height:4677px;overflow:hidden;background:var(--white)}
body{position:relative;font-family:'Roboto',Arial,sans-serif;color:var(--ink)}
.abs{position:absolute}
.heading{font-family:'Jost',Arial,sans-serif;font-weight:600;color:var(--red);text-transform:uppercase;letter-spacing:.5px}
.section-title{left:0;width:1200px;text-align:center;font-size:30px}
.photo{position:absolute}
.brand{font-family:'Jost',Arial,sans-serif;font-weight:500;letter-spacing:5px;text-transform:uppercase;display:flex;align-items:center;gap:14px;white-space:nowrap}
.brand-stack{display:flex;flex-direction:column;line-height:1}
.brand-mark{width:40px;height:40px;background:var(--red);flex:none}
.nav a{font-family:'Jost',Arial,sans-serif;font-weight:500;font-size:16px;text-transform:uppercase;color:var(--ink);text-decoration:none;position:absolute;white-space:nowrap}
.btn{background:var(--red);color:var(--white);font-family:'Jost',Arial,sans-serif;font-weight:600;font-size:18px;text-transform:uppercase;display:flex;align-items:center;justify-content:center;clip-path:polygon(0 10%,100% 0,100% 100%,0 100%)}
.copy{font-size:20px;line-height:34px;color:var(--ink)}
.service-label{font-family:'Jost',Arial,sans-serif;font-weight:600;font-size:19px;color:var(--red);text-transform:uppercase;text-align:center;width:300px}
.service-num{font-family:'Jost',Arial,sans-serif;font-size:64px;color:#f1d6d9;font-weight:500}
.arrow-btn{width:46px;height:46px;border-radius:50%;border:2px solid #e4c3c7;background:var(--white);display:flex;align-items:center;justify-content:center}
.blog-title{font-family:'Jost',Arial,sans-serif;font-weight:600;font-size:20px;color:var(--red);text-transform:uppercase;white-space:nowrap}
.read-more{font-family:'Jost',Arial,sans-serif;font-weight:600;font-size:19px;color:var(--red);text-decoration:underline;text-transform:uppercase}
.date-badge{width:52px;height:68px;text-align:center;color:var(--white);font-family:'Jost',Arial,sans-serif;font-weight:600}
.date-badge .day{background:var(--red);height:38px;font-size:22px;line-height:38px;clip-path:polygon(0 15%,15% 0,85% 0,100% 15%,100% 100%,0 100%)}
.date-badge .mon{background:var(--night);height:30px;font-size:13px;line-height:30px}
.field-label{font-size:14px;color:var(--white);text-transform:uppercase;left:123px}
.field-line{left:111px;width:439px;height:1px;background:rgba(255,255,255,.6)}
.contact-row{left:723px;display:flex;align-items:center;gap:24px;color:var(--white);font-size:20px}
.contact-icon{width:54px;height:54px;border-radius:50%;background:var(--white);display:flex;align-items:center;justify-content:center}
.footer-nav a{position:absolute;color:var(--white);font-family:'Jost',Arial,sans-serif;font-weight:600;font-size:18px;text-transform:uppercase;text-decoration:none;transform:translateX(-50%);white-space:nowrap}
.social{width:16px;height:16px;border-radius:50%;background:var(--white)}
</style>
</head>
<body>

<!-- Hero -->
<svg class="abs" style="left:0;top:0" width="1200" height="640" viewBox="0 0 1200 640">
  <defs>
    <linearGradient id="heroTone" x1="0" y1="0" x2="1" y2="1">
      <stop offset="0" stop-color="#a9c9dc"/>
      <stop offset=".35" stop-color="#3f8fae"/>
      <stop offset=".65" stop-color="#d8cdb8"/>
      <stop offset="1" stop-color="#4d6a3c"/>
    </linearGradient>
  </defs>
  <polygon points="0,0 1200,0 1200,425 975,615 0,532" fill="url(#heroTone)" role="img" aria-label="Coastal town on a cliff above a sandy beach and turquoise sea"/>
  <polygon points="975,615 1200,425 1200,475 1008,615" fill="var(--red)"/>
  <polygon points="860,600 975,615 1008,615 900,608" fill="var(--red-dark)"/>
</svg>
<div class="abs brand" style="left:113px;top:42px;font-size:30px;color:var(--red)">
  <span class="brand-mark"></span>
  <span class="brand-stack"><span>Keelwright</span><span>Builders</span></span>
</div>
<nav class="nav">
  <a style="left:570px;top:62px;color:var(--red)">Home</a>
  <a style="left:653px;top:62px">About Us</a>
  <a style="left:766px;top:62px">Services</a>
  <a style="left:875px;top:62px">Portfolio</a>
  <a style="left:998px;top:62px">Contact Us</a>
</nav>
<h1 class="abs heading" style="left:127px;top:246px;font-size:40px;line-height:51px">Welcome to<br>Keelwright Builders</h1>

<!-- About -->
<div class="photo" style="left:0;top:672px;width:653px;height:471px;background:linear-gradient(135deg,#f3f3f3 0%,#cfcfcf 45%,#8b7a66 100%)" role="img" aria-label="Modern kitchen interior framed inside an outlined building shape"></div>
<h2 class="abs heading" style="left:702px;top:686px;font-size:30px">About Us</h2>
<p class="abs copy" style="left:702px;top:748px;width:415px">Lorem ipsum dolor sit amet, consectetur adipiscing elit, sed do eiusmod tempor incididunt ut labore et dolore magna aliqua. Ut enim ad minim veniam, quis nostrud exercitation ullamco laboris nisi ut aliquip ex ea commodo consequat. Duis aute irure dolor in reprehenderit in voluptate velit esse cillum dolore eu fugiat nulla pariatur.</p>
<a class="abs btn" style="left:702px;top:1060px;width:215px;height:69px">Learn More</a>

<!-- Services -->
<h2 class="abs heading section-title" style="top:1232px">Services</h2>
<svg class="abs" style="left:0;top:1380px" width="1200" height="140" viewBox="0 0 1200 140">
  <path d="M390 70 Q425 50 460 70" fill="none" stroke="#e6b8bd" stroke-width="2" stroke-dasharray="6 6"/>
  <path d="M731 70 Q770 50 806 70" fill="none" stroke="#e6b8bd" stroke-width="2" stroke-dasharray="6 6"/>
</svg>
<span class="abs service-num" style="left:100px;top:1296px">1</span>
<span class="abs service-num" style="left:440px;top:1296px">2</span>
<span class="abs service-num" style="left:790px;top:1296px">3</span>

<div class="abs" style="left:118px;top:1311px;width:272px;height:272px;border-radius:50%;border:3px solid var(--red);padding:8px">
  <div style="width:100%;height:100%;border-radius:50%;background:linear-gradient(160deg,#f2f0ec,#9fb8a6 70%,#4d7a63)" role="img" aria-label="White kitchen with green cabinets"></div>
</div>
<div class="abs" style="left:459px;top:1311px;width:272px;height:272px;border-radius:50%;border:3px solid var(--red);padding:8px">
  <div style="width:100%;height:100%;border-radius:50%;background:linear-gradient(160deg,#d9d3cc,#8a8580 55%,#b89572)" role="img" aria-label="Bathroom with freestanding tub and wood floor"></div>
</div>
<div class="abs" style="left:806px;top:1311px;width:272px;height:272px;border-radius:50%;border:3px solid var(--red);padding:8px">
  <div style="width:100%;height:100%;border-radius:50%;background:linear-gradient(180deg,#b9d3ea,#8a939c 55%,#5d8a4e)" role="img" aria-label="Row of suburban family houses"></div>
</div>

<svg class="abs" style="left:221px;top:1542px" width="66" height="66" viewBox="0 0 66 66">
  <circle cx="33" cy="33" r="31" fill="var(--red)" stroke="#fff" stroke-width="3"/>
  <g fill="none" stroke="#fff" stroke-width="2"><rect x="20" y="19" width="26" height="8"/><rect x="18" y="31" width="30" height="16"/><line x1="33" y1="31" x2="33" y2="47"/></g>
</svg>
<svg class="abs" style="left:562px;top:1542px" width="66" height="66" viewBox="0 0 66 66">
  <circle cx="33" cy="33" r="31" fill="var(--red)" stroke="#fff" stroke-width="3"/>
  <g fill="none" stroke="#fff" stroke-width="2"><path d="M16 33 H50 V38 Q50 46 42 46 H24 Q16 46 16 38 Z"/><path d="M22 33 V20 Q22 16 26 16 Q30 16 30 20"/><line x1="22" y1="46" x2="20" y2="50"/><line x1="44" y1="46" x2="46" y2="50"/></g>
</svg>
<svg class="abs" style="left:909px;top:1542px" width="66" height="66" viewBox="0 0 66 66">
  <circle cx="33" cy="33" r="31" fill="var(--red)" stroke="#fff" stroke-width="3"/>
  <g fill="none" stroke="#fff" stroke-width="2.5" stroke-linejoin="round"><path d="M17 32 L33 18 L49 32"/><path d="M22 28 V47 H44 V28"/><rect x="29" y="36" width="8" height="11"/></g>
</svg>
<div class="abs service-label" style="left:104px;top:1630px">Kitchens</div>
<div class="abs service-label" style="left:445px;top:1630px">Baths</div>
<div class="abs service-label" style="left:792px;top:1630px">Homes</div>

<!-- Dream home -->
<div class="photo" style="left:0;top:1737px;width:1200px;height:510px;background:linear-gradient(180deg,#6f93b8 0%,#b9cbd6 45%,#5f7d4a 75%,#3f5f2e 100%)" role="img" aria-label="Blue roofed single storey house on a green lawn at sunset"></div>
<div class="abs" style="left:22px;top:1773px;width:611px;height:441px;background:var(--white)"></div>
<h2 class="abs heading" style="left:22px;top:1806px;width:611px;text-align:center;font-size:31px;line-height:43px">Designing Your Dream<br>Home Starts Here.</h2>
<p class="abs copy" style="left:84px;top:1910px;width:487px;text-align:center">Lorem ipsum dolor sit amet, consectetur adipiscing elit, sed do eiusmod tempor incididunt ut labore et dolore magna aliqua. Ut enim ad minim veniam, quis nostrud exercitation ullamco laboris nisi ut aliquip ex ea commodo consequat. Duis aute irure dolor in</p>
<a class="abs btn" style="left:220px;top:2114px;width:216px;height:68px">Explore Here</a>

<!-- Portfolio -->
<h2 class="abs heading section-title" style="top:2326px">Portfolio</h2>
<div class="photo" style="left:45px;top:2419px;width:362px;height:269px;background:linear-gradient(135deg,#9a9a98,#e8e6e2 50%,#a88a6c)" role="img" aria-label="Modern bathroom with lit mirror and bathtub"></div>
<div class="photo" style="left:419px;top:2405px;width:361px;height:299px;background:linear-gradient(180deg,#d9dde0,#f1f1ef 50%,#4f7a3a)" role="img" aria-label="White cottage house with dark shutters"></div>
<div class="photo" style="left:791px;top:2419px;width:362px;height:269px;background:linear-gradient(135deg,#f4f2ee,#d6d0c6 55%,#3c3c3c)" role="img" aria-label="Kitchen with white cabinets and dark island"></div>
<div class="abs arrow-btn" style="left:543px;top:2732px">
  <svg width="14" height="14" viewBox="0 0 14 14"><path d="M9 2 L4 7 L9 12" fill="none" stroke="var(--red)" stroke-width="2.5"/></svg>
</div>
<div class="abs arrow-btn" style="left:610px;top:2732px">
  <svg width="14" height="14" viewBox="0 0 14 14"><path d="M5 2 L10 7 L5 12" fill="none" stroke="var(--red)" stroke-width="2.5"/></svg>
</div>

<!-- Testimonials -->
<div class="photo" style="left:0;top:2862px;width:1200px;height:287px;background:linear-gradient(90deg,#1f3320,#2c4a2a 40%,#14201a)" role="img" aria-label="Dark leafy ferns in soft light"></div>
<h2 class="abs heading" style="left:161px;top:2964px;font-size:30px;color:var(--white)">What Our Client Says</h2>
<div class="abs" style="left:601px;top:2951px;width:486px;height:347px;background:var(--red)"></div>
<span class="abs" style="left:560px;top:2960px;font-family:Georgia,serif;font-size:130px;line-height:1;color:#9a9a9a">&ldquo;</span>
<span class="abs" style="left:1055px;top:3190px;font-family:Georgia,serif;font-size:130px;line-height:1;color:#9a9a9a">&rdquo;</span>
<p class="abs" style="left:654px;top:2998px;width:380px;text-align:center;color:var(--white);font-size:20px;line-height:34px">Sed ut perspiciatis unde omnis iste natus error sit voluptatem accusantium doloremque laudantium, totam rem aperiam,</p>
<div class="abs" style="left:708px;top:3158px;width:80px;height:80px;border-radius:50%;background:linear-gradient(135deg,#c9a38a,#5a3b2e);border:3px solid #d8cfc8" role="img" aria-label="Client portrait"></div>
<div class="abs heading" style="left:813px;top:3168px;font-size:20px;color:var(--white)">Lorem Ipsum</div>
<div class="abs" style="left:813px;top:3207px;font-size:20px;color:var(--white)">Managing Director</div>
<svg class="abs" style="left:810px;top:3264px" width="70" height="14" viewBox="0 0 70 14">
  <circle cx="7" cy="7" r="5" fill="#fff"/><circle cx="24" cy="7" r="5" fill="#d9a0a7"/><circle cx="41" cy="7" r="5" fill="#d9a0a7"/><circle cx="58" cy="7" r="5" fill="#d9a0a7"/>
</svg>

<!-- Blog -->
<h2 class="abs heading section-title" style="top:3376px">Latest Blogs and News</h2>

<div class="photo" style="left:111px;top:3463px;width:319px;height:243px;background:linear-gradient(180deg,#f3f2ef,#e6e3dd 60%,#a88d6a)" role="img" aria-label="Clawfoot bathtub in a white bathroom"></div>
<div class="abs date-badge" style="left:140px;top:3449px"><div class="day">14</div><div class="mon">JAN</div></div>
<div class="abs blog-title" style="left:111px;top:3734px">Lorem Ipsum Dolor Sit Amet</div>
<p class="abs copy" style="left:111px;top:3775px;width:300px">Sed ut perspiciatis unde omnis inatus error sit voluptatem accusantium doloremque laudantium, totam rem aperiam,</p>
<div class="abs" style="left:111px;top:3925px"><span class="read-more">Read More</span> <span style="color:var(--red)">&rarr;</span></div>

<div class="photo" style="left:439px;top:3463px;width:320px;height:243px;background:linear-gradient(180deg,#f3f2ef,#e6e3dd 60%,#a88d6a)" role="img" aria-label="Clawfoot bathtub in a white bathroom"></div>
<div class="abs date-badge" style="left:468px;top:3449px"><div class="day">19</div><div class="mon">JUN</div></div>
<div class="abs blog-title" style="left:439px;top:3734px">Lorem Ipsum Dolor Sit Amet</div>
<p class="abs copy" style="left:439px;top:3775px;width:300px">Sed ut perspiciatis unde omnis natus error sit voluptatem accusantium doloremque laudantium, totam rem aperiam,</p>
<div class="abs" style="left:439px;top:3925px"><span class="read-more">Read More</span> <span style="color:var(--red)">&rarr;</span></div>

<div class="photo" style="left:768px;top:3463px;width:319px;height:243px;background:linear-gradient(180deg,#f3f2ef,#e6e3dd 60%,#a88d6a)" role="img" aria-label="Clawfoot bathtub in a white bathroom"></div>
<div class="abs date-badge" style="left:797px;top:3449px"><div class="day">28</div><div class="mon">OCT</div></div>
<div class="abs blog-title" style="left:768px;top:3734px">Lorem Ipsum Dolor Sit Amet</div>
<p class="abs copy" style="left:768px;top:3775px;width:300px">Sed ut perspiciatis unde omnis natus error sit voluptatem accusantium doloremque laudantium, totam rem aperiam,</p>
<div class="abs" style="left:768px;top:3925px"><span class="read-more">Read More</span> <span style="color:var(--red)">&rarr;</span></div>

<!-- Contact -->
<svg class="abs" style="left:0;top:3990px" width="1200" height="460" viewBox="0 0 1200 460">
  <polygon points="0,12 850,76 1200,4 1200,460 0,460" fill="var(--red)"/>
</svg>
<h2 class="abs heading" style="left:111px;top:4068px;font-size:31px;color:var(--white)">Contact Us</h2>
<div class="abs field-label" style="top:4134px">Name</div>
<div class="abs field-line" style="top:4159px"></div>
<div class="abs field-label" style="top:4201px">Email Address</div>
<div class="abs field-line" style="top:4225px"></div>
<div class="abs field-label" style="top:4279px">Message</div>
<div class="abs field-line" style="top:4303px"></div>
<div class="abs" style="left:111px;top:4347px;width:145px;height:67px;background:var(--white);clip-path:polygon(0 10%,100% 0,100% 100%,0 100%);display:flex;align-items:center;justify-content:center;font-family:'Jost',Arial,sans-serif;font-weight:600;font-size:18px;color:var(--night)">SUBMIT</div>
<div class="abs" style="left:599px;top:4075px;width:1px;height:354px;background:rgba(255,255,255,.5)"></div>

<div class="abs contact-row" style="top:4153px">
  <span class="contact-icon"><svg width="24" height="24" viewBox="0 0 24 24"><path d="M6 3 L9 3 L11 8 L8.5 10 Q10 14 14 15.5 L16 13 L21 15 L21 18 Q21 21 18 21 Q3 20 3 6 Q3 3 6 3 Z" fill="var(--red)"/></svg></span>
  <span>+1 888 888 888</span>
</div>
<div class="abs contact-row" style="top:4236px">
  <span class="contact-icon"><svg width="26" height="20" viewBox="0 0 26 20"><rect x="1" y="1" width="24" height="18" rx="2" fill="var(--red)"/><path d="M2 3 L13 11 L24 3" fill="none" stroke="#fff" stroke-width="2"/></svg></span>
  <span>keelwrightbuilders</span>
</div>
<div class="abs contact-row" style="top:4324px">
  <span class="contact-icon"><svg width="20" height="26" viewBox="0 0 20 26"><path d="M10 1 Q19 1 19 10 Q19 16 10 25 Q1 16 1 10 Q1 1 10 1 Z" fill="var(--red)"/><circle cx="10" cy="10" r="3.5" fill="#fff"/></svg></span>
  <span>34, Lorem Ipsum Sit</span>
</div>

<!-- Footer -->
<footer class="abs" style="left:0;top:4445px;width:1200px;height:232px;background:var(--night)">
  <div class="abs brand" style="left:0;top:34px;width:1200px;justify-content:center;font-size:24px;color:var(--white)"><span class="brand-mark" style="width:26px;height:26px"></span>Keelwright Builders</div>
  <nav class="footer-nav">
    <a style="left:301px;top:108px">Home</a>
    <a style="left:425px;top:108px">About Us</a>
    <a style="left:563px;top:108px">Services</a>
    <a style="left:706px;top:108px">Portfolio</a>
    <a style="left:866px;top:108px">Contact Us</a>
  </nav>
  <div class="abs" style="left:111px;top:165px;width:978px;height:1px;background:rgba(255,255,255,.3)"></div>
  <div class="abs" style="left:111px;top:191px;font-size:14px;color:var(--white);text-transform:uppercase">@2023 Copyrights. Keelwright Builders. All Rights Reserved.</div>
  <div class="abs social" style="left:996px;top:193px"></div>
  <div class="abs social" style="left:1034px;top:193px"></div>
  <div class="abs social" style="left:1070px;top:193px"></div>
</footer>

</body>
</html>
```